Q5 Pops (CBD candy infused with Delta-8)

The proposed logo are two pool table balls. One is a D and the other is an 8, its a brand and we need a label for Gummy human treats. This treats are being infused with Delt-8. I i will upload examples only. The example is of the type of labels needed (package and label for bottle)

Target Market(s)

Your professionals

Font styles to use
Sans Serif

Requirements
Must have
• Youthful look
Nice to have
• Consider using the Delta symbol instead of the D.
Also, I provided a sample of a label that's used on two type of packages.

```html
<!DOCTYPE html>
<html lang="en">
<head>
<meta charset="utf-8">
<title>Q5 Pops – Gummy Human Treats</title>
<link rel="stylesheet" href="https://fonts.googleapis.com/css2?family=Fredoka:wght@600&family=Montserrat:wght@700&display=swap">
<style>
  :root {
    --backdrop: #dcd8d6;
    --pouch-red: #d93a3c;
    --pouch-red-dark: #b82c30;
    --label-white: #f6f5f3;
    --band-navy: #2b4270;
    --trim-gold: #e2c24a;
    --brand-maroon: #6e2a35;
    --ink-dark: #1f1f24;
    --treat-white: #ffffff;
  }
  html, body {
    margin: 0;
    padding: 0;
    width: 1200px;
    height: 828px;
    overflow: hidden;
    background: var(--backdrop);
  }
  .canvas {
    position: relative;
    width: 1200px;
    height: 828px;
  }
  .pouch-label {
    position: absolute;
    left: 430px;
    top: 138px;
    width: 340px;
    height: 552px;
  }
  .brand-name {
    font-family: "Fredoka", sans-serif;
    font-weight: 600;
    font-size: 50px;
    fill: var(--brand-maroon);
  }
  .headline {
    font-family: "Fredoka", sans-serif;
    font-weight: 600;
    fill: var(--treat-white);
  }
  .headline--main { font-size: 56px; }
  .headline--sub { font-size: 34px; }
  .net-weight {
    font-family: "Montserrat", sans-serif;
    font-weight: 700;
    font-size: 12.5px;
    fill: var(--ink-dark);
  }
</style>
</head>
<body>
<main class="canvas">
  <svg class="pouch-label" viewBox="0 0 340 552" xmlns="http://www.w3.org/2000/svg">
    <defs>
      <linearGradient id="gummy-tones" x1="0" y1="0" x2="1" y2="0">
        <stop offset="0" stop-color="#e8c23a"/>
        <stop offset="0.2" stop-color="#d8342c"/>
        <stop offset="0.4" stop-color="#f0a826"/>
        <stop offset="0.6" stop-color="#3f8a2e"/>
        <stop offset="0.8" stop-color="#e07a22"/>
        <stop offset="1" stop-color="#c8302a"/>
      </linearGradient>
    </defs>

    <!-- top red zipper band -->
    <rect class="zip-band" x="0" y="0" width="340" height="132" fill="var(--pouch-red)"/>
    <rect x="0" y="0" width="24" height="132" fill="var(--pouch-red-dark)"/>
    <rect x="316" y="0" width="24" height="132" fill="var(--pouch-red-dark)"/>
    <rect class="hang-hole" x="136" y="26" width="68" height="14" rx="7" fill="var(--backdrop)"/>
    <g stroke="var(--pouch-red-dark)" stroke-width="2">
      <line x1="24" y1="80" x2="316" y2="80"/>
      <line x1="24" y1="96" x2="316" y2="96"/>
      <line x1="24" y1="106" x2="316" y2="106"/>
      <line x1="24" y1="122" x2="316" y2="122"/>
    </g>

    <!-- white label body -->
    <rect class="label-body" x="0" y="132" width="340" height="363" fill="var(--label-white)"/>
    <line x1="0" y1="133" x2="340" y2="133" stroke="var(--trim-gold)" stroke-width="3"/>

    <!-- brand -->
    <circle class="brand-dot" cx="58" cy="276" r="14" fill="var(--pouch-red)"/>
    <text class="brand-name" x="84" y="294" textLength="200" lengthAdjust="spacingAndGlyphs">Q5 Pops</text>

    <!-- navy headline band -->
    <path class="headline-band" d="M0 303 Q170 351 340 303 L340 462 Q170 414 0 462 Z" fill="var(--band-navy)"/>
    <path d="M0 303 Q170 351 340 303" fill="none" stroke="var(--trim-gold)" stroke-width="3"/>
    <path d="M0 462 Q170 414 340 462" fill="none" stroke="var(--trim-gold)" stroke-width="3"/>
    <text class="headline headline--main" x="44" y="384" textLength="252" lengthAdjust="spacingAndGlyphs">GUMMY</text>
    <text class="headline headline--sub" x="32" y="426" textLength="278" lengthAdjust="spacingAndGlyphs">HUMAN TREATS</text>

    <text class="net-weight" x="170" y="484" text-anchor="middle">Net Wt. 250g.</text>

    <!-- gummy photo strip -->
    <line x1="0" y1="495" x2="340" y2="495" stroke="var(--trim-gold)" stroke-width="3"/>
    <rect class="gummy-photo" x="0" y="496" width="340" height="56" fill="url(#gummy-tones)" role="img" aria-label="Photo of colourful gummy bears"/>
  </svg>
</main>
</body>
</html>
```